At Home Pet Euthanasia - business cards & brand stationary

We already have a logo and the colors and a website. Need a business card designed that will be able to customized to multiple veterinarians who will be partnering with us. The feel needs to be compassionate, comforting with our tagline 'A Gift of Love at Home'. It will be 2 sides.
On the back our platform/partner vets will be customizing each business card with their own service areas, phone numbers, name and title. On the front, i would like to see experimentation with use of our photos, the logo, tagline and a description 'Peaceful and Compassionate At-Home Pet Euthanasia'

```html
<!DOCTYPE html>
<html lang="en">
<head>
<meta charset="utf-8">
<title>HavenPaw Business Card</title>
<link rel="stylesheet" href="https://fonts.googleapis.com/css2?family=Cinzel:wght@400&family=Raleway:ital,wght@0,700;1,400&family=Arimo:wght@400;700&display=swap">
<style>
  :root {
    --page-bg: #d9dadc;
    --card-white: #ffffff;
    --brand-blue: #7898c0;
    --headline-blue: #7d9ec8;
    --ink: #1c1c1c;
    --front-top: #f3f4f8;
    --front-bottom: #e3ebf4;
    --photo-light: #e3ebf4;
    --photo-mid: #8b98ad;
    --photo-dark: #252e3e;
    --shadow: rgba(0, 0, 0, 0.45);
  }
  * { margin: 0; padding: 0; box-sizing: border-box; }
  html, body {
    width: 1200px; height: 900px; overflow: hidden;
    background: var(--page-bg);
  }
  .stage { position: relative; width: 1200px; height: 900px; }

  .card {
    position: absolute; top: 217px; width: 309px; height: 500px;
    overflow: hidden;
    box-shadow: 2px 3px 3px var(--shadow);
  }

  /* Front */
  .card--front {
    left: 279px;
    border-radius: 0 48px 0 48px;
    background: linear-gradient(180deg, var(--front-top) 0%, var(--front-bottom) 100%);
  }
  .front-headline {
    position: absolute; top: 87px; left: 0; width: 100%;
    text-align: center;
    font-family: "Cinzel", serif; font-weight: 400; font-size: 19px; line-height: 23px;
    color: var(--headline-blue); letter-spacing: 0.3px;
  }
  .front-photo {
    position: absolute; left: 0; top: 190px; width: 100%; height: 310px;
    background: linear-gradient(155deg, var(--photo-light) 0%, var(--photo-light) 22%, var(--photo-mid) 55%, var(--photo-dark) 100%);
  }

  /* Back */
  .card--back {
    left: 617px;
    border-radius: 48px 0 48px 0;
    background: var(--card-white);
  }
  .brand-mark {
    position: absolute; top: 72px; left: 50%; transform: translateX(-50%);
    width: 92px; height: 92px; border-radius: 50%;
    background: var(--brand-blue);
  }
  .brand-name {
    position: absolute; top: 178px; left: 0; width: 100%; text-align: center;
    font-family: "Raleway", sans-serif; font-weight: 700; font-size: 44px;
    color: var(--brand-blue); line-height: 1;
  }
  .brand-tagline {
    position: absolute; top: 237px; left: 0; width: 100%; text-align: center;
    font-family: "Raleway", sans-serif; font-style: italic; font-size: 14.5px;
    color: var(--brand-blue);
  }
  .contact {
    position: absolute; left: 32px; top: 308px;
    font-family: "Arimo", sans-serif; color: var(--ink);
  }
  .contact-name { font-weight: 700; font-size: 21px; color: var(--brand-blue); line-height: 22px; }
  .contact-title { font-size: 14px; line-height: 17px; }
  .contact-lines { list-style: none; margin-top: 14px; }
  .contact-lines li {
    display: flex; align-items: center; gap: 5px;
    font-size: 14.5px; line-height: 18px;
  }
  .contact-lines svg { width: 13px; height: 13px; flex: none; }
  .contact-address { margin-top: 14px; font-size: 15px; line-height: 18px; }
</style>
</head>
<body>
<main class="stage">
  <section class="card card--front">
    <h1 class="front-headline">Peaceful and<br>Compassionate<br>At-Home Pet Euthanasia</h1>
    <div class="front-photo" role="img" aria-label="Photo of an older black dog with a pale blue collar looking upward"></div>
  </section>

  <section class="card card--back">
    <div class="brand-mark"></div>
    <div class="brand-name">HavenPaw</div>
    <p class="brand-tagline">A gift of love at home.</p>

    <div class="contact">
      <p class="contact-name">Daniel Harper</p>
      <p class="contact-title">Managing Director</p>
      <ul class="contact-lines">
        <li>
          <svg viewBox="0 0 16 16" aria-hidden="true"><path d="M3 1.5l3 3-1.5 2c1 2 2.5 3.5 4.5 4.5l2-1.5 3 3-2 2C6 14 2 10 1.5 3.5z" fill="none" stroke="#7898c0" stroke-width="1.6" stroke-linejoin="round"/></svg>
          044-987 654 321
        </li>
        <li>
          <svg viewBox="0 0 16 16" aria-hidden="true"><rect x="1" y="3" width="14" height="10" fill="#7898c0"/><path d="M1 3l7 6 7-6" fill="none" stroke="#fff" stroke-width="1.2"/></svg>
          hello@havenpaw.com
        </li>
        <li>
          <svg viewBox="0 0 16 16" aria-hidden="true"><g fill="none" stroke="#7898c0" stroke-width="1.3"><circle cx="8" cy="8" r="6.5"/><ellipse cx="8" cy="8" rx="3" ry="6.5"/><path d="M1.5 8h13M2.5 5h11M2.5 11h11"/></g></svg>
          www.havenpaw.com
        </li>
      </ul>
      <p class="contact-address">421, Address line goes here<br>45452,Country Name</p>
    </div>
  </section>
</main>
</body>
</html>
```